QuillaVorn needs a dashboard page designed

Redesign the dashboard shown in the provided images.

There are two images:
- dashboard.png
- dashboard-expanded.png

NOTE: The vocabulary navigation on the left will be a very long list of words 100s, so keep that in mind when you're designing both the vocab navigation and the expanded vocab popup.

In the dashboard.png picture, there needs to be a progress chart showing the word progress like the following: review 1(show it as completed) -> review 2(show the user they are here) -> review 3(unvisited) -> review 4(unvisited)

The do-not-design-this-page.png image is for your reference only. It is not to be designed. Use it to understand the overall look and feel of the website to help you create the best dashboard page possible.
Updates

Need extra days to review

Industry/Entity Type

Education English learning

Number of Pages Required

1 page

Requirements
Must have
• The main navigation and main header cannot change between pages. See the do-not-design page for the main navigateion and header.
Should not have
• Do not add a person profile. We will not have images of our users. Keep the icons in the main navigation as they are.

```html
<!DOCTYPE html>
<html lang="en">
<head>
<meta charset="utf-8">
<title>WordNest Tutor — QuillaVorn dashboard</title>
<link href="https://fonts.googleapis.com/css2?family=Poppins:wght@400;500;600;700&display=swap" rel="stylesheet">
<style>
:root{
  --bg:#d4d4d4;
  --green:#6e9f34;
  --ink:#2b333b;
  --rail:#232a31;
  --nav:#2b333b;
  --main:#efefef;
  --card:#ffffff;
  --muted:#9aa3ab;
  --text:#3a3f44;
  --accent:#f0a42a;
  --danger:#e8574a;
}
*{margin:0;padding:0;box-sizing:border-box}
html,body{width:759px;height:1200px;overflow:hidden;background:var(--bg);font-family:'Poppins',sans-serif;color:var(--ink)}
.board{position:relative;width:759px;height:1200px;overflow:hidden}
.board__shapes{position:absolute;inset:0}
.board__title{position:absolute;top:28px;left:0;width:100%;text-align:center;font-size:60px;font-weight:700;letter-spacing:-0.5px;line-height:1;color:var(--ink)}

.screen{position:absolute;left:116px;width:528px;height:455px;border:2px solid #fff;border-radius:9px;overflow:hidden;background:var(--main)}
.screen--top{top:156px}
.screen--bottom{top:660px}
.abs{position:absolute}

.nav-panel{position:absolute;left:0;top:0;width:130px;height:100%;background:var(--nav)}
.rail{position:absolute;left:6px;top:8px;width:34px;height:439px;background:var(--rail);border-radius:7px}
.rail__item{position:absolute;left:0;width:34px;text-align:center;color:#fff;font-size:4px;line-height:1.3}
.rail__home{width:16px;height:16px;border-radius:50%;background:#fff;margin:0 auto 3px;display:flex;align-items:center;justify-content:center}
.rail__rule{position:absolute;left:6px;width:22px;height:0.5px;background:#3d464f}

.vocab-select{position:absolute;left:51px;top:11px;width:50px;height:13px;border:0.6px solid #6b747c;border-radius:2px;color:#fff;font-size:4px;padding:0 5px;display:flex;align-items:center;justify-content:space-between}
.vocab-open{position:absolute;left:118px;top:11px;width:12px;height:12px;border-radius:50%;background:#fff;display:flex;align-items:center;justify-content:center}
.vocab-group{position:absolute;left:51px;width:72px;color:#fff}
.vocab-group__head{font-size:5.3px;font-weight:600;display:flex;justify-content:space-between;align-items:center;white-space:nowrap}
.help{width:5px;height:5px;border:0.5px solid currentColor;border-radius:50%;font-size:3.4px;display:flex;align-items:center;justify-content:center;font-weight:400}
.vocab-group__tag{font-size:4px;font-weight:600;color:var(--green);margin-top:4px}
.vocab-list{list-style:none;margin-top:3px}
.vocab-list li{font-size:4.2px;color:#b8c0c7;line-height:6.6px;white-space:nowrap}
.vocab-list li::before{content:"›";margin-right:4px;color:#d9dde0}
.vocab-rule{position:absolute;left:51px;width:72px;height:0.5px;background:#47515a}

.page-title{position:absolute;left:148px;top:7px;font-size:12px;font-weight:600;color:var(--ink);display:flex;align-items:center;gap:4px;white-space:nowrap}
.header-rule{position:absolute;left:148px;top:43px;width:365px;height:0.6px;background:#d9d9d9}

.steps{position:absolute;left:148px;top:56px}
.step{position:absolute;width:56px;text-align:center;font-size:5px;color:var(--ink);white-space:nowrap}
.step__label{font-size:4.3px;font-weight:500;margin-bottom:3px}
.step__dot{width:24px;height:24px;border-radius:50%;margin:0 auto 4px;border:1px solid var(--ink);background:#fff;display:flex;align-items:center;justify-content:center}
.step__dot--done{background:var(--green);border-color:#fff;box-shadow:0 0 0 0.6px #dfe6d7}
.step__dot--current{background:var(--ink)}
.step__line{position:absolute;top:23px;height:1.4px;background:var(--ink)}

.cta{position:absolute;left:408px;top:113px;width:105px;height:17px;border-radius:9px;background:var(--ink);color:#fff;font-size:3.7px;font-weight:600;display:flex;align-items:center;justify-content:center;gap:3px;white-space:nowrap}
.word-title{position:absolute;left:151px;top:122px;font-size:8.5px;font-weight:600}
.card{position:absolute;left:148px;width:365px;background:var(--card);border-radius:7px}
.card p{font-size:4.8px;line-height:7.7px;color:var(--text)}
.card b{font-weight:600;color:#111}
.section-title{position:absolute;left:148px;font-size:8.6px;font-weight:600;white-space:nowrap}

.chart-band{position:absolute;left:160px;width:342px;font-size:3.8px;color:#7b8288;padding-left:5px;display:flex;align-items:center}
.tip{position:absolute;background:#fff;font-size:3.2px;padding:1.5px 3px;border-radius:1.5px;box-shadow:0 0 2px rgba(0,0,0,.18);white-space:nowrap}
.axis-labels{position:absolute;left:160px;top:335px;width:350px;display:flex;justify-content:space-between;font-size:3.2px;color:#444;white-space:nowrap}
.date-range{position:absolute;left:148px;top:346px;width:365px;text-align:center;font-size:3.8px;font-weight:600}

.overlay{position:absolute;inset:0;background:rgba(20,20,20,.45)}
.modal{position:absolute;left:81px;top:57px;width:368px;height:169px;background:#fff;border-radius:12px}
.modal__select{position:absolute;left:19px;top:14px;width:127px;height:16px;border:0.8px solid #333;border-radius:2px;font-size:4.6px;display:flex;align-items:center;justify-content:space-between;padding:0 7px}
.modal__close{position:absolute;left:348px;top:6px;width:14px;height:14px;border-radius:50%;background:var(--danger);display:flex;align-items:center;justify-content:center}
.modal__rule{position:absolute;left:19px;width:330px;height:0.6px;background:#dadada}
.modal__head{position:absolute;left:19px;font-size:7px;font-weight:600;display:flex;align-items:center;gap:6px;white-space:nowrap}
.modal__head .help{color:#555}
.modal__tag{position:absolute;left:19px;font-size:4px;font-weight:600}
.chips{position:absolute;left:20px;display:flex;gap:3.5px}
.chip{height:11px;padding:0;background:#ececec;border-radius:1.5px;font-size:4.2px;display:flex;align-items:center;justify-content:center;white-space:nowrap}
</style>
</head>
<body>
<div class="board">
  <svg class="board__shapes" width="759" height="1200" viewBox="0 0 759 1200" aria-hidden="true">
    <path d="M0 299 C120 282 260 300 340 330 L340 660 L0 660 Z" fill="#6e9f34"/>
    <path d="M0 660 L116 660 L116 896 C70 905 30 906 0 904 Z" fill="#6e9f34"/>
    <path d="M244 611 L340 611 L336 660 L244 660 Z" fill="#6e9f34"/>
    <path d="M759 886 C700 892 660 900 644 905 L644 1114 L420 1114 C405 1140 395 1170 392 1200 L759 1200 Z" fill="#6e9f34"/>
  </svg>

  <h1 class="board__title">WordNest Tutor</h1>

  <!-- Dashboard -->
  <section class="screen screen--top">
    <div class="nav-panel">
      <div class="rail">
        <div class="rail__item" style="top:15px"><div class="rail__home"><svg width="7" height="7" viewBox="0 0 10 10"><path d="M5 1 L9.5 5 H8 V9 H6 V6.5 H4 V9 H2 V5 H0.5 Z" fill="#232a31"/></svg></div>WordNest<br>Tutor</div>
        <div class="rail__rule" style="top:55px"></div>
        <div class="rail__item" style="top:64px"><svg width="6" height="7" viewBox="0 0 10 12"><path d="M5 0 A4.5 4.5 0 0 1 9.5 4.5 C9.5 8 5 12 5 12 C5 12 0.5 8 0.5 4.5 A4.5 4.5 0 0 1 5 0 Z" fill="#fff"/><circle cx="5" cy="4.5" r="1.7" fill="#232a31"/></svg><br>Daily<br>English</div>
        <div class="rail__rule" style="top:97px"></div>
        <div class="rail__item" style="top:104px"><svg width="7" height="8" viewBox="0 0 10 11"><rect x="1" y="0.5" width="8" height="10" fill="#fff"/><g fill="#232a31"><rect x="2.5" y="2" width="1.5" height="1.5"/><rect x="6" y="2" width="1.5" height="1.5"/><rect x="2.5" y="5" width="1.5" height="1.5"/><rect x="6" y="5" width="1.5" height="1.5"/><rect x="4.2" y="8" width="1.6" height="2.5"/></g></svg><br>Business</div>
      </div>
      <div class="vocab-select">ALL <svg width="4" height="3" viewBox="0 0 6 4"><path d="M0.5 0.5 L3 3 L5.5 0.5" stroke="#fff" fill="none"/></svg></div>
      <div class="vocab-open"><svg width="6" height="6" viewBox="0 0 10 10"><path d="M4 1.5 H1.5 V8.5 H8.5 V6 M6 1.5 H8.5 V4 M8.5 1.5 L4.5 5.5" stroke="#2b333b" fill="none" stroke-width="1"/></svg></div>
      <div class="vocab-group" style="top:35px"><div class="vocab-group__head">Short-Term Memory <span class="help">?</span></div><div class="vocab-group__tag">GRAB</div></div>
      <div class="vocab-rule" style="top:62px"></div>
      <div class="vocab-group" style="top:70px"><div class="vocab-group__head">Working Memory <span class="help">?</span></div>
        <ul class="vocab-list"><li>Cool Down</li><li>Crav</li><li>Go For</li><li>Go-To</li><li>In The Mood For</li><li>Sip</li><li>Soothing</li><li>Stick With</li><li>Throw In/Throw On</li></ul></div>
      <div class="vocab-rule" style="top:148px"></div>
      <div class="vocab-group" style="top:156px"><div class="vocab-group__head">Long-Term Memory <span class="help">?</span></div>
        <ul class="vocab-list"><li>Give ItA Try</li></ul></div>
    </div>

    <div class="page-title">WordNest Tutor <svg width="6" height="4" viewBox="0 0 6 4"><path d="M0.5 0.5 L3 3 L5.5 0.5" stroke="#2b333b" stroke-width="0.9" fill="none"/></svg></div>
    <svg class="abs" style="left:428px;top:15px" width="90" height="16" viewBox="0 0 90 16" aria-hidden="true">
      <circle cx="50" cy="8" r="4.5" fill="none" stroke="#2b333b" stroke-width="0.8"/><path d="M48 8 L49.5 9.5 L52 6.5" fill="none" stroke="#2b333b" stroke-width="0.8"/>
      <circle cx="66" cy="8" r="2" fill="none" stroke="#2b333b" stroke-width="0.8"/><circle cx="66" cy="8" r="4.5" fill="none" stroke="#2b333b" stroke-width="0.8" stroke-dasharray="2 1"/>
      <path d="M78 11 H86 L85 9.5 V7 A3 3 0 0 0 79 7 V9.5 Z M81 12 A1 1 0 0 0 83 12" fill="none" stroke="#2b333b" stroke-width="0.8"/><circle cx="86" cy="5" r="1.8" fill="#efefef" stroke="#2b333b" stroke-width="0.6"/>
    </svg>
    <div class="header-rule"></div>

    <div class="steps">
      <div class="step__line" style="left:14px;width:128px"></div>
      <div class="step__line" style="left:142px;width:64px;background:#d8d8d8"></div>
      <div class="step" style="left:-14px"><div class="step__label">REVIEW 1</div><div class="step__dot step__dot--done"><svg width="10" height="10" viewBox="0 0 10 10"><circle cx="5" cy="5" r="4.3" fill="#fff"/><path d="M3 5 L4.5 6.5 L7 3.8" stroke="#6e9f34" stroke-width="1.1" fill="none"/></svg></div>Completed</div>
      <div class="step" style="left:50px"><div class="step__label">REVIEW 2</div><div class="step__dot step__dot--current"><svg width="9" height="9" viewBox="0 0 10 10"><circle cx="5" cy="3" r="2.3" fill="#fff"/><path d="M1 9.5 A4 4 0 0 1 9 9.5 Z" fill="#fff"/></svg></div>You are here</div>
      <div class="step" style="left:114px"><div class="step__label">REVIEW 3</div><div class="step__dot"></div>Unvisited</div>
      <div class="step" style="left:177px"><div class="step__label">REVIEW 4</div><div class="step__dot"></div>Unvisited</div>
    </div>

    <div class="cta">▶ START VOCABULARY REVIEW EXERCISE 3</div>
    <div class="word-title">Grab <span style="color:var(--accent)">★</span></div>
    <div class="card" style="top:142px;height:49px;padding:8px 14px">
      <p>The word <b>"grab"</b> is most commonly used as a <b>verb</b>, meaning <b>to take something quickly or suddenly</b>. Imagine you're running late for school. You don't have time for breakfast, so you quickly <b>grab</b> an apple from the kitchen and rush out the door. As you reach the bus stop, your friend waves &amp; says, "Hey! Let's <b>grab</b> a coffee after class." Later, when you sit down, your phone starts ringing. You <b>grab</b> it from your bag and answer.</p>
    </div>

    <div class="section-title" style="top:205px">Learning Curve Graph</div>
    <div class="card" style="top:224px;height:133px"></div>
    <div class="chart-band" style="top:233px;height:21px;background:linear-gradient(90deg,#e8ecf1,#f8f9fa)">Long-term Memory</div>
    <div class="chart-band" style="top:254px;height:45px;background:linear-gradient(90deg,#e6efe3,#fafcf9)">Working Memory</div>
    <div class="chart-band" style="top:299px;height:15px;background:linear-gradient(90deg,#f8e9ec,#fdf8f9)">Short-Term Memory</div>
    <div class="chart-band" style="top:314px;height:14px;background:linear-gradient(90deg,#dcebf2,#f7fbfc)">Forgotten Memory</div>
    <svg class="abs" style="left:160px;top:260px" width="355" height="75" viewBox="0 0 355 75" aria-hidden="true">
      <path d="M124 47 C140 48 150 55 154 68" fill="none" stroke="#777" stroke-width="0.5" stroke-dasharray="0.8 1.2"/>
      <path d="M164 5 C210 6 240 25 239 68" fill="none" stroke="#777" stroke-width="0.5" stroke-dasharray="0.8 1.2"/>
      <rect x="122" y="46" width="3" height="22" rx="1" fill="#2b333b"/>
      <rect x="162" y="4" width="3" height="64" rx="1" fill="#2b333b"/>
      <line x1="0" y1="68" x2="342" y2="68" stroke="#999" stroke-width="0.5"/>
      <g stroke="#999" stroke-width="0.5">
        <line x1="6" y1="68" x2="6" y2="72"/><line x1="26" y1="68" x2="26" y2="72"/><line x1="45" y1="68" x2="45" y2="72"/><line x1="64" y1="68" x2="64" y2="72"/><line x1="84" y1="68" x2="84" y2="72"/><line x1="103" y1="68" x2="103" y2="72"/><line x1="123" y1="68" x2="123" y2="72"/><line x1="142" y1="68" x2="142" y2="72"/><line x1="162" y1="68" x2="162" y2="72"/><line x1="181" y1="68" x2="181" y2="72"/><line x1="200" y1="68" x2="200" y2="72"/><line x1="220" y1="68" x2="220" y2="72"/><line x1="239" y1="68" x2="239" y2="72"/><line x1="259" y1="68" x2="259" y2="72"/><line x1="278" y1="68" x2="278" y2="72"/><line x1="298" y1="68" x2="298" y2="72"/><line x1="317" y1="68" x2="317" y2="72"/><line x1="337" y1="68" x2="337" y2="72"/>
      </g>
    </svg>
    <div class="tip" style="left:276px;top:297px">21 May</div>
    <div class="tip" style="left:314px;top:251px">22 May</div>
    <div class="axis-labels"><span>18 May</span><span>12:00</span><span>19 May</span><span>12:00</span><span>20 May</span><span>12:00</span><span>21 May</span><span>12:00</span><span>22 May</span><span>12:00</span><span>23 May</span><span>12:00</span><span>24 May</span><span>12:00</span><span>25 May</span><span>12:00</span><span>26 May</span><span>12:00</span></div>
    <div class="date-range">DATE RANGE</div>

    <div class="section-title" style="top:370px">WordNest Tutor Learning Analysis</div>
    <div class="card" style="top:388px;height:43px;padding:8px 12px">
      <p>Lorem ipsum <b>dolor</b> sit amet, consectetur adipiscing elit. Nam r<b>utrum commodo</b> enim id bibendum. Nunc dignissim risus <b>dolor</b>nec finibus dictum eu. Aliquam sit amet euismod metus, quis malesuada erat. Sed at felis quis nulla feugiat cursus at at <b>dolor</b>. Maecenas pretium aliquet dapibus. Fusce et eleifend massa. &nbsp;Sed convallis ex mi, at lobortis ligula congue vel.</p>
    </div>
  </section>

  <!-- Dashboard with vocabulary popup -->
  <section class="screen screen--bottom">
    <div class="nav-panel">
      <div class="rail">
        <div class="rail__item" style="top:15px"><div class="rail__home"><svg width="7" height="7" viewBox="0 0 10 10"><path d="M5 1 L9.5 5 H8 V9 H6 V6.5 H4 V9 H2 V5 H0.5 Z" fill="#232a31"/></svg></div>WordNest<br>Tutor</div>
        <div class="rail__rule" style="top:55px"></div>
        <div class="rail__item" style="top:64px"><svg width="6" height="7" viewBox="0 0 10 12"><path d="M5 0 A4.5 4.5 0 0 1 9.5 4.5 C9.5 8 5 12 5 12 C5 12 0.5 8 0.5 4.5 A4.5 4.5 0 0 1 5 0 Z" fill="#fff"/><circle cx="5" cy="4.5" r="1.7" fill="#232a31"/></svg><br>Daily<br>English</div>
        <div class="rail__rule" style="top:97px"></div>
        <div class="rail__item" style="top:104px"><svg width="7" height="8" viewBox="0 0 10 11"><rect x="1" y="0.5" width="8" height="10" fill="#fff"/><g fill="#232a31"><rect x="2.5" y="2" width="1.5" height="1.5"/><rect x="6" y="2" width="1.5" height="1.5"/><rect x="2.5" y="5" width="1.5" height="1.5"/><rect x="6" y="5" width="1.5" height="1.5"/><rect x="4.2" y="8" width="1.6" height="2.5"/></g></svg><br>Business</div>
      </div>
      <div class="vocab-select">ALL <svg width="4" height="3" viewBox="0 0 6 4"><path d="M0.5 0.5 L3 3 L5.5 0.5" stroke="#fff" fill="none"/></svg></div>
      <div class="vocab-open"><svg width="6" height="6" viewBox="0 0 10 10"><path d="M4 1.5 H1.5 V8.5 H8.5 V6 M6 1.5 H8.5 V4 M8.5 1.5 L4.5 5.5" stroke="#2b333b" fill="none" stroke-width="1"/></svg></div>
      <div class="vocab-group" style="top:35px"><div class="vocab-group__head">Short-Term Memory <span class="help">?</span></div><div class="vocab-group__tag">GRAB</div></div>
      <div class="vocab-rule" style="top:62px"></div>
      <div class="vocab-group" style="top:70px"><div class="vocab-group__head">Working Memory <span class="help">?</span></div>
        <ul class="vocab-list"><li>Cool Down</li><li>Crav</li><li>Go For</li><li>Go-To</li><li>In The Mood For</li><li>Sip</li><li>Soothing</li><li>Stick With</li><li>Throw In/Throw On</li></ul></div>
      <div class="vocab-rule" style="top:148px"></div>
      <div class="vocab-group" style="top:156px"><div class="vocab-group__head">Long-Term Memory <span class="help">?</span></div>
        <ul class="vocab-list"><li>Give ItA Try</li></ul></div>
    </div>

    <div class="page-title">WordNest Tutor <svg width="6" height="4" viewBox="0 0 6 4"><path d="M0.5 0.5 L3 3 L5.5 0.5" stroke="#2b333b" stroke-width="0.9" fill="none"/></svg></div>
    <svg class="abs" style="left:428px;top:15px" width="90" height="16" viewBox="0 0 90 16" aria-hidden="true">
      <circle cx="50" cy="8" r="4.5" fill="none" stroke="#2b333b" stroke-width="0.8"/><path d="M48 8 L49.5 9.5 L52 6.5" fill="none" stroke="#2b333b" stroke-width="0.8"/>
      <circle cx="66" cy="8" r="2" fill="none" stroke="#2b333b" stroke-width="0.8"/><circle cx="66" cy="8" r="4.5" fill="none" stroke="#2b333b" stroke-width="0.8" stroke-dasharray="2 1"/>
      <path d="M78 11 H86 L85 9.5 V7 A3 3 0 0 0 79 7 V9.5 Z M81 12 A1 1 0 0 0 83 12" fill="none" stroke="#2b333b" stroke-width="0.8"/><circle cx="86" cy="5" r="1.8" fill="#efefef" stroke="#2b333b" stroke-width="0.6"/>
    </svg>
    <div class="header-rule"></div>

    <div class="cta">▶ START VOCABULARY REVIEW EXERCISE 3</div>
    <div class="card" style="top:142px;height:49px;padding:8px 14px">
      <p>The word <b>"grab"</b> is most commonly used as a <b>verb</b>, meaning <b>to take something quickly or suddenly</b>. Imagine you're running late for school. You don't have time for breakfast, so you quickly <b>grab</b> an apple from the kitchen and rush out the door. As you reach the bus stop, your friend waves &amp; says, "Hey! Let's <b>grab</b> a coffee after class." Later, when you sit down, your phone starts ringing. You <b>grab</b> it from your bag and answer.</p>
    </div>
    <div class="card" style="top:224px;height:133px"></div>
    <div class="chart-band" style="top:233px;height:21px;background:linear-gradient(90deg,#e8ecf1,#f8f9fa)">Long-term Memory</div>
    <div class="chart-band" style="top:254px;height:45px;background:linear-gradient(90deg,#e6efe3,#fafcf9)">Working Memory</div>
    <div class="chart-band" style="top:299px;height:15px;background:linear-gradient(90deg,#f8e9ec,#fdf8f9)">Short-Term Memory</div>
    <div class="chart-band" style="top:314px;height:14px;background:linear-gradient(90deg,#dcebf2,#f7fbfc)">Forgotten Memory</div>
    <svg class="abs" style="left:160px;top:260px" width="355" height="75" viewBox="0 0 355 75" aria-hidden="true">
      <path d="M124 47 C140 48 150 55 154 68" fill="none" stroke="#777" stroke-width="0.5" stroke-dasharray="0.8 1.2"/>
      <path d="M164 5 C210 6 240 25 239 68" fill="none" stroke="#777" stroke-width="0.5" stroke-dasharray="0.8 1.2"/>
      <rect x="122" y="46" width="3" height="22" rx="1" fill="#2b333b"/>
      <rect x="162" y="4" width="3" height="64" rx="1" fill="#2b333b"/>
      <line x1="0" y1="68" x2="342" y2="68" stroke="#999" stroke-width="0.5"/>
    </svg>
    <div class="tip" style="left:276px;top:297px">21 May</div>
    <div class="tip" style="left:314px;top:251px">22 May</div>
    <div class="axis-labels"><span>18 May</span><span>12:00</span><span>19 May</span><span>12:00</span><span>20 May</span><span>12:00</span><span>21 May</span><span>12:00</span><span>22 May</span><span>12:00</span><span>23 May</span><span>12:00</span><span>24 May</span><span>12:00</span><span>25 May</span><span>12:00</span><span>26 May</span><span>12:00</span></div>
    <div class="date-range">DATE RANGE</div>
    <div class="section-title" style="top:370px">WordNest Tutor Learning Analysis</div>
    <div class="card" style="top:388px;height:43px;padding:8px 12px">
      <p>Lorem ipsum <b>dolor</b> sit amet, consectetur adipiscing elit. Nam r<b>utrum commodo</b> enim id bibendum. Nunc dignissim risus <b>dolor</b>nec finibus dictum eu. Aliquam sit amet euismod metus, quis malesuada erat. Sed at felis quis nulla feugiat cursus at at <b>dolor</b>. Maecenas pretium aliquet dapibus. Fusce et eleifend massa. &nbsp;Sed convallis ex mi, at lobortis ligula congue vel.</p>
    </div>

    <div class="overlay"></div>

    <div class="modal">
      <div class="modal__select">ALL <svg width="5" height="3" viewBox="0 0 6 4"><path d="M0.5 0.5 L3 3 L5.5 0.5" stroke="#333" fill="none"/></svg></div>
      <div class="modal__close"><svg width="6" height="6" viewBox="0 0 6 6"><path d="M1 1 L5 5 M5 1 L1 5" stroke="#fff" stroke-width="0.9"/></svg></div>
      <div class="modal__rule" style="top:41px"></div>
      <div class="modal__head" style="top:48px">Short-Term Memory <span class="help">?</span></div>
      <div class="modal__tag" style="top:62px">GRAB</div>
      <div class="modal__rule" style="top:76px"></div>
      <div class="modal__head" style="top:84px">Working Memory <span class="help">?</span></div>
      <div class="chips" style="top:99px">
        <span class="chip" style="width:29px">Cool Down</span><span class="chip" style="width:27px">Crav</span><span class="chip" style="width:29px">Go For</span><span class="chip" style="width:29px">Go-To</span><span class="chip" style="width:44px">In The Mood For</span><span class="chip" style="width:26px">Sip</span><span class="chip" style="width:32px">Soothing</span><span class="chip" style="width:32px">Stick With</span><span class="chip" style="width:52px">Throw In/Throw On</span>
      </div>
      <div class="modal__rule" style="top:120px"></div>
      <div class="modal__head" style="top:127px">Long-Term Memory <span class="help">?</span></div>
      <div class="chips" style="top:143px"><span class="chip" style="width:36px">Give ItA Try</span></div>
    </div>
  </section>
</div>
</body>
</html>
```